Hollow Lantern: Ebbtide -> Album artwork!

We are a rock band out of Washington DC, and need a CD cover design for our debut album titled "Ebbtide". We have strong psychedelic rock and grunge influences (Velvet Marrow to Thornbelly), so perhaps something with some dark but trippy geometric designs, abstract modern art, etc.

The album deals with a protagonist's fall from grace after a traumatic event; worsening engagement in self destructive behavior to cope, only to reach peace and enlightenment at the end...before re-entering in to the whole cycle again. Any type of imagery or artwork that might help illustrate that cyclical nature would be of interest, but certainly not mandatory. Icarus mythology an interesting parallel.

We'd like our band name "Hollow Lantern" to appear on the album cover and CD disc art, but in a subtle fashion so the artwork and design can take precedence for the viewer. We'd also like the album name "Ebbtide" to appear on the cover, middle binding, and CD disc please, but secondary to the band name.

If you'd like to hear the music from the album, it is posted here: www.fanpagehub.net/HollowLanternBand

Target Market(s)

Non-trendy rock and roll fans, strong roots in classic rock to grunge, more artsy than commercial.

Industry/Entity Type

Fashion

Requirements
Must have
• Song list for rear cover:
• 1. Paper Harbor
• 2. Kindling
• 3. Glass Moth
• 4. Quiet Birches
• 5. Under Your Roof
• 6. Hand It Over
• 7. Open Ledger
• 8. Out of Plain Sight
• 9. Vapor
• 10. Ember Wheel
• Also, would like a black and white photo montage of band members on inside cover please, raw photos attached to project.
Should not have
• Phoenixes, Yin Yang circles

```html
<!DOCTYPE html>
<html lang="en">
<head>
<meta charset="utf-8">
<title>Hollow Lantern — Ebbtide Disc Art</title>
<link rel="stylesheet" href="https://fonts.googleapis.com/css2?family=Antonio:wght@200&display=swap">
<style>
  :root {
    --page: #ffffff;
    --marble-light: #b2b2b2;
    --marble-mid: #a0a0a0;
    --marble-dark: #8a8a8a;
    --figure-dark: #0c0c0c;
    --hub-ring: #ffffff;
    --band-type: #e4e4e4;
  }
  html, body {
    margin: 0;
    padding: 0;
    width: 1000px;
    height: 1200px;
    overflow: hidden;
    background: var(--page);
  }
  .disc-art {
    display: block;
    width: 1000px;
    height: 1200px;
  }
  .surface-light { stop-color: var(--marble-light); }
  .surface-mid { stop-color: var(--marble-mid); }
  .surface-dark { stop-color: var(--marble-dark); }
  .figure-core { stop-color: var(--figure-dark); stop-opacity: 0.92; }
  .figure-edge { stop-color: var(--figure-dark); stop-opacity: 0; }
  .hub-ring {
    fill: var(--hub-ring);
    opacity: 0.26;
  }
  .spindle-hole {
    fill: var(--page);
  }
  .band-name {
    font-family: "Antonio", "Arial Narrow", sans-serif;
    font-weight: 200;
    font-size: 80px;
    fill: var(--band-type);
    text-transform: uppercase;
  }
</style>
</head>
<body>
<svg class="disc-art" viewBox="0 0 1000 1200" xmlns="http://www.w3.org/2000/svg">
  <defs>
    <radialGradient id="disc-surface" cx="50%" cy="50%" r="50%">
      <stop offset="0%" class="surface-light"/>
      <stop offset="60%" class="surface-mid"/>
      <stop offset="100%" class="surface-dark"/>
    </radialGradient>
    <radialGradient id="figure-shadow" cx="50%" cy="50%" r="50%">
      <stop offset="0%" class="figure-core"/>
      <stop offset="55%" class="figure-core"/>
      <stop offset="100%" class="figure-edge"/>
    </radialGradient>
    <clipPath id="disc-clip">
      <circle cx="500" cy="597" r="475"/>
    </clipPath>
  </defs>

  <circle class="disc-surface" cx="500" cy="597" r="475" fill="url(#disc-surface)"
          role="img" aria-label="Mirrored grey marble texture covering the disc"/>

  <g class="falling-figure-area" clip-path="url(#disc-clip)">
    <ellipse cx="500" cy="590" rx="200" ry="470" transform="rotate(-12 500 590)"
             fill="url(#figure-shadow)"
             role="img"
             aria-label="Black faceted geometric figure falling headfirst through the centre of the disc"/>
  </g>

  <circle class="hub-ring" cx="500" cy="597" r="192"/>
  <circle class="spindle-hole" cx="500" cy="597" r="98"/>

  <text class="band-name band-name--first" x="96" y="630"
        textLength="150" lengthAdjust="spacingAndGlyphs">Hollow</text>
  <text class="band-name band-name--second" x="748" y="630"
        textLength="172" lengthAdjust="spacingAndGlyphs">Lantern</text>
</svg>
</body>
</html>
```